Recipe mobile app, new flow and design for uploading recipe process

I need a new recipe upload process that's simple, intuitive, and engaging.
The goal is to have a user-friendly and fast flow.
The app is a social recipe library where anyone can upload a recipe after signing up. I currently have a flow, but it's "boring," so I'd like to significantly improve this aspect of the app.
When I create a new recipe, it's immediately saved and labeled as a draft. I'll then need to specify:
- Recipe title
- Cover image (required)
- Number of people (how many people is the recipe for)
- Ingredients (name, quantity, and unit of measurement)
- Recipe explanation (broken down into steps, and I can optionally attach an image to each step)
- Upload
Every change is immediately saved, so you can edit, exit, and resume editing later.
I've attached images of the app and the current upload process.
Thank you.
Low design quality
Good morning everyone,
some of the designs received are fantastic, but please make sure to carefully read the requirement so as not to do extra work.
The requirement is to redesign the flow that a user follows when uploading a recipe to the platform.
We have uploaded the current app screens to give you an idea of what the product looks like, what the colors and style are, but we don’t need a full redesign - only the part mentioned above, while keeping the existing style and colors (we cannot rework the entire theme).
To clarify: if you look at the screens shared in the zip file attached to the project, the focus should be on the screens from 5_.png to 10_.png.
These screens can be redesigned in the most creative way you think, as long as the overall theme remains unchanged.
Thank you for your attention.

```html
<!DOCTYPE html>
<html lang="en">
<head>
<meta charset="utf-8">
<title>Recipe App – Upload Flow</title>
<link href="https://fonts.googleapis.com/css2?family=Inter:wght@400;500;600&display=swap" rel="stylesheet">
<style>
:root{
  --stage:#111111;
  --label:#22a45a;
  --screen:#f1f4f0;
  --card:#ffffff;
  --ink:#1c1c1c;
  --muted:#8b8f8a;
  --line:#e2e5e1;
  --accent:#f7894a;
  --accent-soft:#fde3d3;
  --grey-btn:#7b7d7b;
  --pasta-a:#f4f1ea;--pasta-b:#e8c45a;
  --curry-a:#3a2a22;--curry-b:#c9642a;
  --taco-a:#8a5a3a;--taco-b:#d9a86a;
  --green-a:#4f5a44;--green-b:#c4c8b4;
  --red-a:#c8352a;--red-b:#f07b58;
  --pan-a:#3e3a36;--pan-b:#bfb8a8;
}
*{box-sizing:border-box;margin:0;padding:0}
html,body{width:1200px;height:1200px;overflow:hidden;background:var(--stage)}
body{font-family:"Inter",sans-serif;color:var(--ink)}
.board{position:absolute;left:0;top:0;width:1932px;height:1932px;transform:scale(.6211);transform-origin:0 0}
.label{position:absolute;top:231px;width:165px;height:25px;background:var(--label);color:#fff;font-size:10px;font-weight:500;display:flex;align-items:center;justify-content:center}
.screen{position:absolute;top:283px;width:173px;background:var(--screen);border-radius:3px;overflow:hidden}
.ico{width:8px;height:8px;fill:none;stroke:currentColor;stroke-width:1.6;stroke-linecap:round;stroke-linejoin:round}
.topbar{height:36px;background:var(--card);display:flex;align-items:center;justify-content:center;position:relative;font-size:9px;font-weight:500}
.topbar .back{position:absolute;left:7px;top:14px}
.topbar .right{position:absolute;right:7px;top:14px}
.ph{display:block;border-radius:3px}
.ph.pasta{background:radial-gradient(circle at 50% 55%,var(--pasta-b) 0 28%,var(--pasta-a) 45%,#cfcac0 75%,#9a9488)}
.ph.curry{background:radial-gradient(circle at 50% 50%,var(--curry-b) 0 30%,#6a3a22 45%,var(--curry-a) 70%)}
.ph.taco{background:linear-gradient(135deg,var(--taco-a),var(--taco-b) 55%,#e7d3a8)}
.ph.chicken{background:radial-gradient(circle at 50% 50%,#d07a36 0 35%,#5b3a24 65%,#2a221e)}
.ph.green{background:radial-gradient(circle at 50% 50%,var(--green-b) 0 35%,var(--green-a) 70%)}
.ph.bolo{background:radial-gradient(circle at 50% 50%,#c9542e 0 22%,#e6c48a 40%,#ddd6cb 70%)}
.ph.pizza{background:linear-gradient(135deg,#b8482e,#e2a25a 60%,#f0d9a8)}
.ph.cake{background:linear-gradient(135deg,#3b2a24,#b89a7a 60%,#eee)}
.ph.tomato{background:radial-gradient(circle at 45% 55%,var(--red-a) 0 30%,var(--red-b) 50%,#e9e3da 75%)}
.ph.pan{background:radial-gradient(circle at 50% 45%,var(--pan-b) 0 35%,var(--pan-a) 75%)}
.ph.boil{background:radial-gradient(circle at 50% 40%,#f3c64a 0 25%,#6a5a3a 55%,#1e1a16)}
.ph.avatar{border-radius:50%;background:radial-gradient(circle at 50% 40%,#c79a7a,#5a3a2a)}
.pad{padding:0 7px}
.h-sec{font-size:9.5px;font-weight:500;margin:9px 0 5px}
.tiny{font-size:4.6px;color:var(--muted)}
.sm{font-size:5.8px}
.navbar{position:absolute;left:0;right:0;bottom:0;height:32px;background:var(--card);display:flex;justify-content:space-around;padding-top:5px}
.navbar .it{display:flex;flex-direction:column;align-items:center;font-size:4.3px;color:var(--muted);gap:3px}
.navbar .it.on{color:var(--accent)}
.navbar::after{content:"";position:absolute;left:60px;bottom:3px;width:53px;height:2px;border-radius:2px;background:#555}
.progress{padding:8px 7px 0}
.progress .row{display:flex;justify-content:space-between;font-size:6px}
.progress .bar{height:3px;background:var(--line);border-radius:2px;margin-top:4px}
.progress .bar i{display:block;height:100%;background:var(--accent);border-radius:2px}
.btn{position:absolute;left:7px;right:7px;height:22px;border-radius:2px;background:var(--accent);color:#fff;font-size:6.5px;display:flex;align-items:center;justify-content:center}
.btn.grey{background:var(--grey-btn)}
.field-label{font-size:6px;font-weight:500;margin:8px 0 4px}
.field-label b{color:var(--accent);font-weight:400}
.input{height:18px;background:var(--card);border:1px solid var(--line);border-radius:2px;font-size:5px;color:var(--muted);display:flex;align-items:center;padding:0 6px}
/* home */
.greet{display:flex;align-items:center;gap:4px;padding:14px 7px 0}
.greet .ph{width:18px;height:18px}
.greet b{display:block;font-size:8.5px;font-weight:500}
.search{margin:8px 7px 0;height:17px;background:var(--card);border:1px solid var(--line);border-radius:2px;display:flex;align-items:center;gap:5px;padding:0 5px;font-size:5px;color:var(--muted)}
.pop{display:flex;gap:7px;padding-left:7px}
.pop .card{width:93px;background:var(--card);padding:5px;flex-shrink:0}
.pop .ph{height:60px}
.pop .t{font-size:5.2px;margin-top:4px}
.row-card{margin:0 7px 6px;background:var(--card);display:flex;align-items:center;gap:6px;padding:3px}
.row-card .ph{width:50px;height:34px}
/* recipe */
.hero{height:115px;position:relative}
.heart{position:absolute;right:4px;top:6px;width:11px;height:11px;background:#fff;border-radius:2px;color:var(--red-a);display:flex;align-items:center;justify-content:center}
.stats{display:flex;justify-content:space-around;padding:12px 8px 0;text-align:center;font-size:6px}
.stats svg{width:14px;height:14px;display:block;margin:0 auto 3px}
.ing{list-style:none}
.ing li{display:flex;gap:5px;font-size:5.6px;line-height:7px;margin-bottom:4px}
.ing li::before{content:"";flex:0 0 6px;height:6px;border:1px solid #aaa;border-radius:1px;margin-top:.5px}
.ing li span{color:#555}
.steps{padding-left:13px}
.step{margin-bottom:8px}
.step h4{font-size:6.4px;font-weight:500;display:flex;gap:5px;align-items:center;margin-left:-7px;margin-bottom:5px}
.step h4 svg{color:var(--label);width:8px;height:8px}
.step p{font-size:4.9px;line-height:7.3px;color:var(--muted)}
.step .ph{height:72px;margin-top:4px;width:142px}
.foot{display:flex;justify-content:center;gap:18px;font-size:6px;margin-top:12px;align-items:center}
.foot span{display:flex;gap:2px;align-items:center}
/* search */
.tabs{display:flex;margin:10px 7px 0;border-bottom:1px solid var(--line);font-size:6px;color:var(--muted)}
.tabs div{flex:1;text-align:center;padding-bottom:5px}
.tabs .on{color:var(--ink);border-bottom:1.5px solid var(--accent)}
.grid{display:grid;grid-template-columns:1fr 1fr;gap:8px 6px;padding:0 7px}
.grid .ph{height:60px}
.grid .t{font-size:5.2px;margin-top:4px}
/* upload */
.drop{margin-top:0;height:85px;border:1px dashed #cfd2cf;background:var(--card);display:flex;flex-direction:column;align-items:center;justify-content:center;font-size:6.2px}
.drop svg{width:18px;height:18px;margin-bottom:9px}
.counter{display:flex;align-items:center;justify-content:center;gap:14px;margin-top:22px}
.counter .c{width:13px;height:13px;border-radius:50%;background:#d8dbd7;display:flex;align-items:center;justify-content:center;font-size:8px;color:#444}
.counter .n{font-size:28px;font-weight:300}
.group{background:var(--card);margin-bottom:1px;padding:6px 7px;position:relative}
.group b{font-size:7px;font-weight:500;display:block}
.group .edit{position:absolute;right:10px;top:10px;color:#555}
.addbox{border:1px dashed #cfd2cf;padding:6px;margin-top:8px}
.addbox .row{display:flex;gap:4px}
.addbox .input{flex:1;height:15px;font-size:4.6px}
.addbox .add{width:30px;height:15px;background:var(--accent);color:#fff;font-size:5px;border-radius:2px;display:flex;align-items:center;justify-content:center}
.stepblk{display:flex;gap:10px;margin-bottom:10px}
.stepblk .num{display:flex;flex-direction:column;align-items:center;gap:4px}
.stepblk .num i{width:11px;height:11px;border-radius:50%;background:var(--accent);color:#fff;font-style:normal;font-size:5px;display:flex;align-items:center;justify-content:center}
.stepblk .num em{font-style:normal;font-size:6px;color:#bbb;letter-spacing:-1px;line-height:4px}
.stepblk .box{flex:1;background:var(--card);padding:6px}
.stepblk .area{height:34px;background:var(--screen);font-size:5px;color:var(--muted);padding:6px}
.photo-btn{margin-top:6px;height:18px;border:1px dashed #cfd2cf;display:flex;align-items:center;gap:5px;padding:0 7px;font-size:6.2px}
.fab{width:22px;height:22px;border-radius:50%;background:var(--accent);color:#fff;margin:4px auto 0;display:flex;align-items:center;justify-content:center}
.table{background:var(--card);padding:5px 5px 2px}
.table .tr{display:flex;justify-content:space-between;font-size:4.6px;line-height:6px;margin-bottom:5px;gap:8px}
.table .tr span:last-child{text-align:right}
.table .th{font-size:5.8px;font-weight:500}
/* profile */
.pf{text-align:center;padding-top:3px}
.pf .ph{width:55px;height:55px;margin:0 auto}
.pf h2{font-size:11px;font-weight:500;margin-top:4px}
.pf .stat{font-size:4.6px;margin-top:4px;color:#555}
.pf .stat b{color:var(--ink);font-weight:600}
</style>
</head>
<body>
<svg width="0" height="0" style="position:absolute">
<defs>
<symbol id="i-back" viewBox="0 0 10 10"><path d="M6.5 1.5 3 5l3.5 3.5"/></symbol>
<symbol id="i-bookmark" viewBox="0 0 10 10"><path d="M2.5 1h5v8L5 7 2.5 9z"/></symbol>
<symbol id="i-search" viewBox="0 0 10 10"><circle cx="4.3" cy="4.3" r="3"/><path d="m6.5 6.5 2.5 2.5"/></symbol>
<symbol id="i-home" viewBox="0 0 10 10"><path d="M1.5 4.5 5 1.5l3.5 3V9h-7z"/></symbol>
<symbol id="i-plus" viewBox="0 0 10 10"><circle cx="5" cy="5" r="4"/><path d="M5 3v4M3 5h4"/></symbol>
<symbol id="i-user" viewBox="0 0 10 10"><circle cx="5" cy="3.3" r="2"/><path d="M1.5 9c.5-2 2-3 3.5-3s3 1 3.5 3"/></symbol>
<symbol id="i-heart" viewBox="0 0 10 10"><path d="M5 8.5 1.5 5A2 2 0 0 1 5 2.5 2 2 0 0 1 8.5 5z"/></symbol>
<symbol id="i-chat" viewBox="0 0 10 10"><path d="M1.5 5a3.5 3.5 0 1 1 1.5 2.9L1.5 8.5l.5-1.6A3.5 3.5 0 0 1 1.5 5z"/></symbol>
<symbol id="i-check" viewBox="0 0 10 10"><path d="m1.5 5.2 2.3 2.3 4.7-5"/></symbol>
<symbol id="i-pencil" viewBox="0 0 10 10"><path d="M2 8l.5-2L7 1.5 8.5 3 4 7.5z"/></symbol>
<symbol id="i-camera" viewBox="0 0 20 20"><path d="M2 6h4l1.5-2h5L14 6h4v10H2z"/><circle cx="10" cy="11" r="3"/></symbol>
<symbol id="i-gear" viewBox="0 0 10 10"><circle cx="5" cy="5" r="1.5"/><path d="M5 1v1.3M5 7.7V9M1 5h1.3M7.7 5H9M2.2 2.2l.9.9M6.9 6.9l.9.9M2.2 7.8l.9-.9M6.9 3.1l.9-.9"/></symbol>
<symbol id="i-people" viewBox="0 0 14 14"><circle cx="4.5" cy="4.5" r="2"/><circle cx="9.5" cy="4.5" r="2"/><path d="M1 12c0-2 1.5-3.5 3.5-3.5S8 10 8 12M6 12c0-2 1.5-3.5 3.5-3.5S13 10 13 12"/></symbol>
<symbol id="i-clock" viewBox="0 0 14 14"><circle cx="7" cy="7" r="5.5"/><path d="M7 4v3.5l2 1.5"/></symbol>
<symbol id="i-pot" viewBox="0 0 14 14"><path d="M2 6h10v5.5H2zM1 6h12M5 2.5v2M7 1.5v3M9 2.5v2"/></symbol>
<symbol id="i-image" viewBox="0 0 10 10"><rect x="1.5" y="2" width="7" height="6" rx="1"/><path d="m2 7.5 2.2-2.2 1.6 1.4 1-1 1.6 1.6"/></symbol>
<symbol id="i-x" viewBox="0 0 10 10"><path d="m2.5 2.5 5 5M7.5 2.5l-5 5"/></symbol>
<symbol id="i-up" viewBox="0 0 10 10"><path d="m2 6.5 3-3 3 3"/></symbol>
<symbol id="i-minus" viewBox="0 0 10 10"><path d="M3 5h4"/></symbol>
<symbol id="i-add" viewBox="0 0 10 10"><path d="M5 2v6M2 5h6"/></symbol>
</defs>
</svg>

<main class="board">
  <div class="label" style="left:197px">Home Page</div>
  <div class="label" style="left:381px">Recipe Page</div>
  <div class="label" style="left:565px">Search Results page</div>
  <div class="label" style="left:746px">Upload Recipe Step_1</div>
  <div class="label" style="left:930px">Upload Recipe Step_2</div>
  <div class="label" style="left:1112px">Upload Recipe Step_3</div>
  <div class="label" style="left:1293px">Upload Recipe Step_4</div>
  <div class="label" style="left:1476px">Upload Recipe Step_5</div>
  <div class="label" style="left:1661px">Profile Page</div>

  <!-- Home -->
  <section class="screen" style="left:195px;height:385px">
    <div class="greet"><span class="ph avatar" role="img" aria-label="User profile photo"></span><div><span class="tiny">Good Morning!</span><b>Milo</b></div></div>
    <div class="search"><svg class="ico"><use href="#i-search"/></svg>Search for recipes...</div>
    <h3 class="h-sec pad">Popular Recipes</h3>
    <div class="pop">
      <div class="card"><span class="ph pasta" role="img" aria-label="Creamy tomato pasta on a plate"></span><div class="t">Creamy Tomato Pasta</div><div class="tiny">By Chef Renata</div></div>
      <div class="card"><span class="ph chicken" role="img" aria-label="Butter chicken in a pan"></span><div class="t">Butter Chicken</div><div class="tiny">By Chef Oskar</div></div>
    </div>
    <h3 class="h-sec pad">New Uploads</h3>
    <div class="row-card"><span class="ph taco" role="img" aria-label="Spicy chicken tacos"></span><div><div class="sm">Spicy Chicken Tocos</div><div class="tiny">By Chef Tomas</div></div></div>
    <div class="row-card"><span class="ph cake" role="img" aria-label="Vegan chocolate cake"></span><div><div class="sm">Vegan Chocolate Cake</div><div class="tiny">By Chef Mira</div></div></div>
    <h3 class="h-sec pad" style="margin-top:8px">Saved Recipes</h3>
    <div class="row-card"><span class="ph pizza" role="img" aria-label="Margherita pizza"></span><div><div class="sm">Classic Margherita Pizza</div><div class="tiny">By Chef Jonah</div></div></div>
    <nav class="navbar">
      <div class="it on"><svg class="ico"><use href="#i-home"/></svg>Home</div>
      <div class="it"><svg class="ico"><use href="#i-search"/></svg>Search</div>
      <div class="it"><svg class="ico"><use href="#i-plus"/></svg>Upload</div>
      <div class="it"><svg class="ico"><use href="#i-bookmark"/></svg>Saved</div>
      <div class="it"><svg class="ico"><use href="#i-user"/></svg>Profile</div>
    </nav>
  </section>

  <!-- Recipe -->
  <section class="screen" style="left:378px;height:1365px">
    <div class="topbar"><svg class="ico back"><use href="#i-back"/></svg><svg class="ico right"><use href="#i-bookmark"/></svg></div>
    <div class="hero ph pasta" style="border-radius:0" role="img" aria-label="Creamy tomato pasta served on a white plate"><span class="heart"><svg class="ico" style="fill:currentColor;stroke:none"><use href="#i-heart"/></svg></span></div>
    <div class="pad">
      <h1 style="font-size:12.5px;font-weight:500;margin-top:6px">Creamy Tomato Pasta</h1>
      <div class="tiny" style="display:flex;gap:3px;align-items:center;margin-top:3px"><span class="ph avatar" style="width:9px;height:9px" role="img" aria-label="Chef photo"></span>By Chef Renata • 2d ago</div>
      <div class="stats">
        <div><svg class="ico"><use href="#i-people"/></svg>4 Serving</div>
        <div><svg class="ico"><use href="#i-clock"/></svg>30 Min</div>
        <div><svg class="ico"><use href="#i-pot"/></svg>Easy</div>
      </div>
      <h3 class="h-sec" style="margin-top:14px">Ingredients</h3>
      <ul class="ing">
        <li><div>Pasta <span>– 200g (e.g., penne, fettuccine, or spaghetti)</span></div></li>
        <li><div>Olive oil <span>– 1 tbsp</span></div></li>
        <li><div>Garlic <span>– 2 cloves, minced</span></div></li>
        <li><div>Onion <span>– 1 small, finely chopped (optional)</span></div></li>
        <li><div>Tomato puree or crushed tomatoes <span>– 1 cup (about 240ml)</span></div></li>
        <li><div>Heavy cream <span>– ½ cup (120ml)</span></div></li>
        <li><div>Grated Parmesan cheese <span>– ¼ cup (optional but recommended)</span></div></li>
        <li><div>Salt <span>– to taste</span></div></li>
        <li><div>Black pepper <span>– to taste</span></div></li>
        <li><div>Red chili flakes <span>– ½ tsp (optional for a kick)</span></div></li>
        <li><div>Pasta water <span>– ¼ cup (reserve from boiling pasta)</span></div></li>
        <li><div>Butter <span>– 1 tbsp (optional, for richness)</span></div></li>
      </ul>
      <h3 class="h-sec" style="margin-top:8px">Instuctions</h3>
      <div class="steps">
        <div class="step"><h4><svg class="ico"><use href="#i-check"/></svg>Step 1: Boil the Pasta</h4><p>Bring a large pot of salted water to a boil. Add your choice of pasta (about 200g) and cook until al dente. Before draining, reserve about ¼ cup of pasta water to use later in the sauce. Set the drained pasta aside.</p><span class="ph boil" role="img" aria-label="Pasta being dropped into boiling water"></span></div>
        <div class="step"><h4><svg class="ico"><use href="#i-check"/></svg>Step 2: Sauté Garlic and Onion</h4><p>In a large pan, heat 1 tablespoon of olive oil over medium heat. Add minced garlic (and chopped onion if using) and sauté for 2–3 minutes until fragrant and slightly golden.</p><span class="ph pan" role="img" aria-label="Garlic and onion sautéing in a pan"></span></div>
        <div class="step"><h4><svg class="ico"><use href="#i-check"/></svg>Step 3: Add Tomato Base</h4><p>Pour in 1 cup of tomato puree or crushed tomatoes. Let it simmer for 5–7 minutes, allowing the sauce to thicken slightly. Season with salt, pepper, red chili flakes, and dried basil or oregano for flavor.</p><span class="ph tomato" role="img" aria-label="Tomato puree poured into a pot"></span></div>
        <div class="step"><h4><svg class="ico"><use href="#i-check"/></svg>Step 4: Make It Creamy</h4><p>Lower the heat and stir in ½ cup of heavy cream. Mix until the sauce turns a creamy pink. Add 1 tablespoon of butter for extra richness, and use the reserved pasta water to adjust the consistency if needed.</p><span class="ph tomato" role="img" aria-label="Bowl of creamy tomato sauce with fresh tomatoes"></span></div>
        <div class="step"><h4><svg class="ico"><use href="#i-check"/></svg>Step 5: Mix Pasta and Sauce</h4><p>Add the cooked pasta directly into the sauce. Toss well to coat each piece evenly. Stir in grated Parmesan cheese if desired and let it melt into the sauce for a creamy finish.</p><span class="ph tomato" role="img" aria-label="Pasta tossed in sauce in a pan"></span></div>
        <div class="step"><h4><svg class="ico"><use href="#i-check"/></svg>Step 6: Garnish and Serve</h4><p>Serve the pasta hot, garnished with fresh basil leaves and extra Parmesan. Add a drizzle of olive oil or a sprinkle of chili flakes if you like a little heat.</p><span class="ph pasta" role="img" aria-label="Finished pasta plated"></span></div>
      </div>
      <div class="foot">
        <span><svg class="ico"><use href="#i-heart"/></svg>201</span>
        <span><svg class="ico"><use href="#i-chat"/></svg>49</span>
        <span><svg class="ico"><use href="#i-bookmark"/></svg>300</span>
      </div>
    </div>
  </section>

  <!-- Search results -->
  <section class="screen" style="left:562px;height:498px">
    <div class="topbar"><svg class="ico back"><use href="#i-back"/></svg>Search Results</div>
    <div class="search" style="color:var(--ink)"><svg class="ico"><use href="#i-search"/></svg><span style="flex:1">Pasta</span><svg class="ico"><use href="#i-x"/></svg></div>
    <div class="tabs"><div class="on">Recipes</div><div>People</div></div>
    <p class="tiny pad" style="margin:9px 0 6px">Showing 12 Results for "Pasta"</p>
    <div class="grid">
      <div><span class="ph pasta" role="img" aria-label="Creamy tomato pasta"></span><div class="t">Creamy Tomato Pasta</div><div class="tiny">By Chef Renata</div></div>
      <div><span class="ph curry" role="img" aria-label="Chicken biryani"></span><div class="t">Chicken Biryani</div><div class="tiny">By Chef Priya</div></div>
      <div><span class="ph bolo" role="img" aria-label="Spaghetti bolognese"></span><div class="t">Spaghetti Bolognese</div><div class="tiny">By Chef Karim</div></div>
      <div><span class="ph taco" role="img" aria-label="Beef tacos"></span><div class="t">Beef Tacos</div><div class="tiny">By Chef Oskar</div></div>
      <div><span class="ph chicken" role="img" aria-label="Butter chicken"></span><div class="t">Butter Chicken</div><div class="tiny">By Chef Renata</div></div>
      <div><span class="ph green" role="img" aria-label="Thai green curry"></span><div class="t">Thai Green Curry</div><div class="tiny">By Chef Renata</div></div>
      <div><span class="ph chicken" role="img" aria-label="Butter chicken"></span></div>
      <div><span class="ph green" role="img" aria-label="Thai green curry"></span></div>
    </div>
    <nav class="navbar">
      <div class="it"><svg class="ico"><use href="#i-home"/></svg>Home</div>
      <div class="it on"><svg class="ico"><use href="#i-search"/></svg>Search</div>
      <div class="it"><svg class="ico"><use href="#i-plus"/></svg>Upload</div>
      <div class="it"><svg class="ico"><use href="#i-bookmark"/></svg>Saved</div>
      <div class="it"><svg class="ico"><use href="#i-user"/></svg>Profile</div>
    </nav>
  </section>

  <!-- Upload step 1 -->
  <section class="screen" style="left:745px;height:385px">
    <div class="topbar"><svg class="ico back"><use href="#i-back"/></svg>New Recipe</div>
    <div class="progress"><div class="row"><span>Step 1 of 5</span><span>20%</span></div><div class="bar"><i style="width:20%"></i></div></div>
    <div class="pad">
      <div class="field-label">Recipe Title <b>*</b></div>
      <div class="input">Enter recipe title</div>
      <div class="field-label" style="margin-top:10px">Cover Image <b>*</b></div>
      <div class="drop"><svg class="ico"><use href="#i-camera"/></svg>Tap to upload a photo<span class="tiny" style="margin-top:3px">PNG, JPG, or GIF up to 10MB</span></div>
    </div>
    <div class="btn" style="top:349px">Next</div>
  </section>

  <!-- Upload step 2 -->
  <section class="screen" style="left:928px;height:385px">
    <div class="topbar"><svg class="ico back"><use href="#i-back"/></svg>New Recipe</div>
    <div class="progress"><div class="row"><span>Step 2 of 5</span><span>40%</span></div><div class="bar"><i style="width:40%"></i></div></div>
    <h3 class="pad" style="font-size:10px;font-weight:500;margin-top:11px;line-height:14px">How many people is this recipe for?</h3>
    <div class="counter"><span class="c"><svg class="ico" style="width:7px;height:7px"><use href="#i-minus"/></svg></span><span class="n">4</span><span class="c"><svg class="ico" style="width:7px;height:7px"><use href="#i-add"/></svg></span></div>
    <div class="btn" style="top:349px">Next</div>
  </section>

  <!-- Upload step 3 -->
  <section class="screen" style="left:1111px;height:425px">
    <div class="topbar"><svg class="ico back"><use href="#i-back"/></svg>New Recipe</div>
    <div class="progress"><div class="row"><span>Step 3 of 5</span><span>60%</span></div><div class="bar"><i style="width:60%"></i></div></div>
    <div class="pad">
      <h3 class="h-sec" style="margin-top:10px">Ingredients</h3>
      <div class="group"><b style="font-size:8px">Cake</b><span class="tiny">4 ingredients</span><svg class="ico edit"><use href="#i-pencil"/></svg></div>
      <div class="group" style="margin-top:4px"><b>Flour</b><span class="tiny">1 cup</span><svg class="ico edit"><use href="#i-pencil"/></svg></div>
      <div class="group"><b>Sugar</b><span class="tiny">1 cup</span><svg class="ico edit"><use href="#i-pencil"/></svg></div>
      <div class="group"><b>Eggs</b><span class="tiny">2</span><svg class="ico edit"><use href="#i-pencil"/></svg></div>
      <div class="group"><b>Baking Powder</b><span class="tiny">1 tsp</span><svg class="ico edit"><use href="#i-pencil"/></svg></div>
      <div class="group" style="margin-top:8px"><b style="font-size:8px">Frosting</b><span class="tiny">3 ingredients</span><svg class="ico edit"><use href="#i-up"/></svg></div>
      <div class="addbox">
        <div class="row"><div class="input">Add Ingredient (e.g., 1 cup flour)</div><div class="add">Add</div></div>
        <div style="display:flex;justify-content:space-between;margin-top:6px;font-size:4.8px;align-items:center">
          <span style="display:flex;gap:3px;align-items:center"><i style="width:5px;height:5px;border:1px solid #bbb;display:inline-block"></i>As Needed</span>
          <span style="color:var(--accent)">+ New Group</span>
        </div>
      </div>
    </div>
    <div class="btn" style="top:382px">Next</div>
  </section>

  <!-- Upload step 4 -->
  <section class="screen" style="left:1294px;height:471px">
    <div class="topbar"><svg class="ico back"><use href="#i-back"/></svg>New Recipe</div>
    <div class="progress"><div class="row"><span>Step 4 of 5</span><span>80%</span></div><div class="bar"><i style="width:80%"></i></div></div>
    <div class="pad">
      <h3 class="h-sec" style="margin-top:10px">Steps</h3>
      <div class="stepblk"><div class="num"><i>1</i><em>⋮⋮</em></div><div class="box"><div class="area">Describe this step...</div><div class="photo-btn"><svg class="ico"><use href="#i-image"/></svg>Add Photo (optional)</div></div></div>
      <div class="stepblk"><div class="num"><i>2</i><em>⋮⋮</em></div><div class="box"><div class="area">Describe this step...</div><span class="ph pasta" style="height:49px;margin-top:6px" role="img" aria-label="Attached photo of pasta for this step"></span></div></div>
      <div class="stepblk"><div class="num"><i>2</i><em>⋮⋮</em></div><div class="box"><div class="area">Describe this step...</div><div class="photo-btn"><svg class="ico"><use href="#i-image"/></svg>Add Photo (optional)</div></div></div>
      <div class="fab"><svg class="ico" style="width:11px;height:11px"><use href="#i-add"/></svg></div>
    </div>
    <div class="btn grey" style="top:429px">Next</div>
  </section>

  <!-- Upload step 5 -->
  <section class="screen" style="left:1477px;height:933px">
    <div class="topbar"><svg class="ico back"><use href="#i-back"/></svg>Review Recipe</div>
    <div class="progress"><div class="row"><span>Step 5 of 5</span><span>100%</span></div><div class="bar"><i style="width:100%"></i></div></div>
    <div class="pad">
      <h1 style="font-size:12px;font-weight:500;line-height:17px;margin-top:9px">Classic Chocolate Chip Cookies</h1>
      <div style="display:flex;justify-content:space-between;font-size:6px;margin-top:3px"><span>Serves: 24 Cookies</span><span style="color:var(--accent);margin-right:13px">✎ Edit</span></div>
    </div>
    <span class="ph pasta" style="height:109px;border-radius:0;margin-top:6px" role="img" aria-label="Cover photo of the recipe"></span>
    <div class="pad">
      <h3 class="h-sec" style="margin-top:9px">Ingredients</h3>
      <div class="table">
        <div class="tr th"><span>Ingredients</span><span>Net Amount</span></div>
        <div class="tr"><span>All -purpose flour</span><span>2 ¼ cups (280g)</span></div>
        <div class="tr"><span>Baking soda</span><span>1 tsp</span></div>
        <div class="tr"><span>Salt</span><span>½ tsp</span></div>
        <div class="tr"><span>Unsalted butter (softened)</span><span>1 cup (227g / 2 sticks)</span></div>
        <div class="tr"><span>Granulated sugar</span><span>¾ cup (150g)</span></div>
        <div class="tr"><span>Brown sugar (packed)</span><span>¾ cup (165g)</span></div>
        <div class="tr"><span>Eggs</span><span>2 large</span></div>
        <div class="tr"><span>Vanilla extract</span><span>2 tsp</span></div>
        <div class="tr"><span>Semi-sweet chocolate chips</span><span>2 cups (340g)</span></div>
      </div>
      <div class="steps" style="margin-top:10px">
        <div class="step"><h4><svg class="ico"><use href="#i-check"/></svg>Step 1: Preheat the Oven</h4><p>Preheat your oven to 375°F (190°C). Line a baking tray with parchment paper or a silicone baking mat.</p></div>
        <div class="step"><h4><svg class="ico"><use href="#i-check"/></svg>Step 2: Mix Dry Ingredients</h4><p>In a medium bowl, whisk together 2¼ cups flour, 1 tsp baking soda, and ½ tsp salt. Set it aside.</p></div>
        <div class="step"><h4><svg class="ico"><use href="#i-check"/></svg>Step 3: Cream Butter and Sugars</h4><p>In a large bowl, beat 1 cup softened butter, ¾ cup white sugar, and ¾ cup brown sugar together until the mixture is smooth and creamy (about 2–3 minutes).</p></div>
        <div class="step"><h4><svg class="ico"><use href="#i-check"/></svg>Step 4: Add Eggs and Vanilla</h4><p>Add 2 eggs, one at a time, beating well after each. Stir in 2 tsp vanilla extract until fully combined.</p></div>
        <div class="step"><h4><svg class="ico"><use href="#i-check"/></svg>Step 5: Combine Wet and Dry</h4><p>Gradually add the dry ingredients to the wet mixture. Mix until everything is well combined and a dough forms.</p></div>
        <div class="step"><h4><svg class="ico"><use href="#i-check"/></svg>Step 6: Add Chocolate Chips</h4><p>Stir in 2 cups of chocolate chips (and ½ cup nuts if using) evenly throughout the dough.</p></div>
        <div class="step"><h4><svg class="ico"><use href="#i-check"/></svg>Step 7: Shape the Cookies</h4><p>Scoop about 1 tablespoon of dough for each cookie and place them on the prepared baking sheet, leaving about 2 inches of space between each.</p></div>
        <div class="step"><h4><svg class="ico"><use href="#i-check"/></svg>Step 8: Bake</h4><p>Bake for 9–11 minutes, or until the edges are golden brown but the centers are still soft.</p></div>
        <div class="step"><h4><svg class="ico"><use href="#i-check"/></svg>Step 9: Cool and Serve</h4><p>Let the cookies cool on the baking tray for a few minutes, then transfer to a wire rack to cool completely. Enjoy warm or store in an airtight container.</p></div>
      </div>
    </div>
    <div class="btn" style="top:893px">Upload Recipe</div>
  </section>

  <!-- Profile -->
  <section class="screen" style="left:1660px;height:498px">
    <div class="topbar"><svg class="ico back"><use href="#i-back"/></svg>Lena Ward<svg class="ico right"><use href="#i-gear"/></svg></div>
    <div class="pf">
      <span class="ph avatar" role="img" aria-label="Profile photo"></span>
      <h2>Lena Ward</h2>
      <div class="tiny" style="color:#555">Foodie | Recipe Creator</div>
      <div class="stat"><b>123</b> Recipes &nbsp;• <b>12k</b> Followers &nbsp;• <b>26</b> Following</div>
    </div>
    <div class="tabs" style="margin-bottom:12px"><div class="on" style="flex:0 0 50px">Recipes</div><div style="flex:0 0 28px">Draft</div><div style="flex:0 0 44px">Saved</div><div></div></div>
    <div class="grid">
      <div><span class="ph pasta" role="img" aria-label="Creamy tomato pasta"></span><div class="t">Creamy Tomato Pasta</div><div class="tiny">By Chef Renata</div></div>
      <div><span class="ph curry" role="img" aria-label="Chicken biryani"></span><div class="t">Chicken Biryani</div><div class="tiny">By Chef Renata</div></div>
      <div><span class="ph bolo" role="img" aria-label="Spaghetti bolognese"></span><div class="t">Spaghetti Bolognese</div><div class="tiny">By Chef Renata</div></div>
      <div><span class="ph taco" role="img" aria-label="Beef tacos"></span><div class="t">Beef Tacos</div><div class="tiny">By Chef Renata</div></div>
      <div><span class="ph chicken" role="img" aria-label="Butter chicken"></span><div class="t">Butter Chicken</div><div class="tiny">By Chef Renata</div></div>
      <div><span class="ph green" role="img" aria-label="Thai green curry"></span><div class="t">Thai Green Curry</div><div class="tiny">By Chef Renata</div></div>
    </div>
    <nav class="navbar">
      <div class="it"><svg class="ico"><use href="#i-home"/></svg>Home</div>
      <div class="it"><svg class="ico"><use href="#i-search"/></svg>Search</div>
      <div class="it"><svg class="ico"><use href="#i-plus"/></svg>Upload</div>
      <div class="it"><svg class="ico"><use href="#i-bookmark"/></svg>Saved</div>
      <div class="it on"><svg class="ico"><use href="#i-user"/></svg>Profile</div>
    </nav>
  </section>
</main>
</body>
</html>
```